Business Card Design - Commercial Photographer

Professional Photographer requires eye catching creative business card. The design will need to incorporate my current logo in some form & not clash with my website tones & colours ( although website will be re designed in the future ). I'm currently shooting new folios in Commercial, Fashion & Architecture so I'm marketing to professional clients rather than portrait / wedding clients. Looking for something professional & creative.

Industry/Entity Type

Marketing

Requirements
Must have
• Website address - www.brightlenswork.com.au

Phone number - 0471586039

Email - info@brightlenswork.com.au

```html
<!DOCTYPE html>
<html lang="en">
<head>
<meta charset="utf-8">
<title>Bright Lens Work Photography – Business Cards</title>
<link rel="stylesheet" href="https://fonts.googleapis.com/css2?family=Arimo:wght@400;700&family=Open+Sans:wght@400;600&display=swap">
<style>
  :root {
    --stage: #3a2a1d;
    --card-black: #050505;
    --card-sheen: #2a2a2a;
    --card-edge: #e9e9e9;
    --mark-grey: #4a4a4a;
    --logo-silver: #d9d9d9;
    --text-white: #f2f2f2;
    --text-soft: #bdbdbd;
    --rule: #8a8a8a;
  }
  * { box-sizing: border-box; margin: 0; padding: 0; }
  html, body { width: 1200px; height: 913px; overflow: hidden; }
  body {
    background: var(--stage);
    font-family: "Open Sans", Arial, sans-serif;
    position: relative;
  }
  .card {
    position: absolute;
    width: 525px;
    height: 300px;
    top: 306px;
    border-radius: 3px;
    overflow: hidden;
    background:
      linear-gradient(115deg, var(--card-black) 0%, var(--card-black) 38%, var(--card-sheen) 46%, var(--card-black) 54%, var(--card-black) 100%);
    box-shadow: 0 3px 0 var(--card-edge), 0 18px 36px rgba(0,0,0,.55);
  }
  .card--front { left: 50px; }
  .card--back  { left: 625px; }

  .logo {
    position: absolute;
    display: flex;
    align-items: center;
    gap: 14px;
  }
  .logo__square {
    width: 62px;
    height: 62px;
    background: var(--mark-grey);
    flex: none;
  }
  .logo__name {
    font-family: "Arimo", Arial, sans-serif;
    font-weight: 700;
    color: var(--logo-silver);
    text-transform: uppercase;
    line-height: 1.05;
    white-space: nowrap;
  }
  .logo__name span { display: block; }
  .logo__main { font-size: 27px; letter-spacing: 1px; }
  .logo__sub  { font-size: 14px; letter-spacing: 3px; text-align: right; }

  .card--front .logo { left: 112px; top: 118px; }

  .card--back .logo { left: 24px; top: 196px; gap: 12px; }
  .card--back .logo__square { width: 46px; height: 46px; }
  .card--back .logo__main { font-size: 18px; letter-spacing: .5px; }
  .card--back .logo__sub { font-size: 10px; letter-spacing: 2.5px; }

  .divider {
    position: absolute;
    left: 0; top: 0;
    width: 525px; height: 300px;
  }

  .contact {
    position: absolute;
    left: 345px;
    top: 40px;
    width: 168px;
    color: var(--text-white);
  }
  .contact__name { font-weight: 600; font-size: 16px; white-space: nowrap; }
  .contact__title { font-size: 13px; color: var(--text-soft); margin: 2px 0 16px 20px; }
  .contact__list { list-style: none; font-size: 10.5px; line-height: 16px; }
  .contact__list li { display: flex; align-items: center; gap: 7px; white-space: nowrap; }
  .contact__list svg { width: 10px; height: 10px; flex: none; fill: var(--text-white); }
  .contact__address { font-size: 10.5px; line-height: 15px; color: var(--text-soft); margin-top: 12px; }
</style>
</head>
<body>
  <section class="card card--front" aria-label="Business card front">
    <div class="logo">
      <div class="logo__square"></div>
      <div class="logo__name"><span class="logo__main">Bright Lens Work</span><span class="logo__sub">Photography</span></div>
    </div>
  </section>

  <section class="card card--back" aria-label="Business card back">
    <svg class="divider" viewBox="0 0 525 300" aria-hidden="true">
      <line x1="250" y1="20" x2="330" y2="280" stroke="var(--rule)" stroke-width="1"/>
    </svg>
    <div class="logo">
      <div class="logo__square"></div>
      <div class="logo__name"><span class="logo__main">Bright Lens Work</span><span class="logo__sub">Photography</span></div>
    </div>
    <div class="contact">
      <p class="contact__name">Your Long Name</p>
      <p class="contact__title">Your Title</p>
      <ul class="contact__list">
        <li><svg viewBox="0 0 10 10"><path d="M2 1h2l1 2-1 1a5 5 0 0 0 2 2l1-1 2 1v2c0 1-1 1-1 1A8 8 0 0 1 1 2s0-1 1-1z"/></svg>000 0 0 000 00</li>
        <li><svg viewBox="0 0 10 10"><rect x="1" y="3" width="8" height="5"/><rect x="3" y="1" width="4" height="2"/></svg>(00) 0 0 0000 0000</li>
        <li><svg viewBox="0 0 10 10"><path d="M1 2h8v6H1z M1 2l4 3 4-3" stroke="#050505" stroke-width=".6"/></svg>yourname@yourwebsite.com</li>
        <li><svg viewBox="0 0 10 10"><circle cx="5" cy="5" r="4"/><path d="M1 5h8M5 1v8" stroke="#050505" stroke-width=".6"/></svg>www.yourwebsite.com</li>
      </ul>
      <p class="contact__address">Your office or residential address in just two line with pin code.</p>
    </div>
  </section>
</body>
</html>
```